Velbrin Industries Digital Flyer

Digital Flyers for a machine shop, preferably PDF format.

Looking for a futuristic look/layout

Target Market(s)

Tier 1 and 2 Military, Defense contractors, Medical, Space, Microsatellite

Industry/Entity Type

Ultra-high precision machining of complex, mission critical components. Primary industries are defense, aerospace, space, micro-satellites, satellites

Font styles to use
Serif

Colors
0054AA
0677BA
7BADD7
CADEEF
E8F1F8

```html
<!DOCTYPE html>
<html lang="en">
<head>
<meta charset="utf-8">
<title>Velbrin Industries – Our Services</title>
<link rel="stylesheet" href="https://fonts.googleapis.com/css2?family=Roboto+Serif:wdth,wght@50..150,300..700&family=Roboto:wght@400;700&display=swap">
<style>
  :root {
    --blue-deep: #0054AA;
    --blue-mid: #0677BA;
    --blue-soft: #7BADD7;
    --blue-pale: #CADEEF;
    --blue-mist: #E8F1F8;
    --navy: #0b4a8c;
    --teal: #27b8b0;
    --grey-bg: #e6e7e9;
    --grey-light: #f4f4f5;
    --ink: #2f3338;
    --white: #ffffff;
  }
  * { margin: 0; padding: 0; box-sizing: border-box; }
  html, body { width: 860px; height: 1200px; overflow: hidden; background: var(--white); }
  .flyer {
    position: relative;
    width: 860px;
    height: 1200px;
    overflow: hidden;
    font-family: "Roboto", Arial, sans-serif;
    color: var(--ink);
    background: linear-gradient(180deg, var(--grey-light) 0%, var(--grey-bg) 100%);
  }
  .serif {
    font-family: "Roboto Serif", Georgia, serif;
    font-stretch: 75%;
    font-variation-settings: "wdth" 75;
  }
  .backdrop { position: absolute; inset: 0; }

  .brand {
    position: absolute;
    top: 46px;
    left: 545px;
    display: flex;
    align-items: center;
    gap: 14px;
    color: var(--blue-pale);
    font-weight: 400;
  }
  .brand__dot { width: 50px; height: 50px; border-radius: 50%; background: var(--blue-pale); }
  .brand__name { line-height: 1; text-transform: uppercase; }
  .brand__name span { display: block; }
  .brand__name .line-1 { font-size: 38px; letter-spacing: 0.5px; }
  .brand__name .line-2 { font-size: 22px; margin-top: 3px; }

  .headline {
    position: absolute;
    left: 57px;
    top: 648px;
    color: var(--blue-deep);
  }
  .headline__title { font-size: 45px; font-weight: 400; line-height: 48px; letter-spacing: 0.3px; }
  .headline__sub { font-size: 25px; font-weight: 400; margin-top: 10px; letter-spacing: 0.2px; }

  .services { position: absolute; top: 866px; left: 57px; display: flex; }
  .service { display: flex; gap: 18px; width: 268px; }
  .service__icon { width: 46px; height: 46px; flex: none; }
  .service__title {
    font-weight: 700;
    font-size: 12.5px;
    color: var(--ink);
    margin-top: 6px;
    margin-bottom: 8px;
  }
  .service__text { font-size: 9.5px; line-height: 15px; color: var(--ink); width: 150px; }

  .contact { position: absolute; left: 62px; top: 1076px; list-style: none; font-size: 11.5px; color: var(--ink); }
  .contact li { display: flex; align-items: center; gap: 17px; height: 24px; }
  .contact svg { width: 15px; height: 15px; fill: var(--navy); fill-rule: evenodd; }

  .quote {
    position: absolute;
    left: 291px;
    top: 1064px;
    color: var(--blue-deep);
    font-size: 21px;
    line-height: 27px;
  }

  .social { position: absolute; left: 700px; top: 1130px; display: flex; gap: 21px; list-style: none; }
  .social li { width: 22px; height: 22px; border-radius: 50%; background: var(--white); }
</style>
</head>
<body>
<main class="flyer">
  <svg class="backdrop" width="860" height="1200" viewBox="0 0 860 1200">
    <defs>
      <linearGradient id="panelBlue" x1="0" y1="0" x2="1" y2="1">
        <stop offset="0" stop-color="#0677BA"/>
        <stop offset="0.6" stop-color="#0054AA"/>
        <stop offset="1" stop-color="#0b4a8c"/>
      </linearGradient>
      <linearGradient id="cornerBlue" x1="0" y1="1" x2="1" y2="0">
        <stop offset="0" stop-color="#0054AA"/>
        <stop offset="1" stop-color="#0677BA"/>
      </linearGradient>
      <linearGradient id="turbineTone" x1="0" y1="0" x2="1" y2="1">
        <stop offset="0" stop-color="#3a2c16"/>
        <stop offset="0.5" stop-color="#c9932e"/>
        <stop offset="1" stop-color="#1c1a18"/>
      </linearGradient>
      <linearGradient id="gearTone" x1="0" y1="0" x2="1" y2="1">
        <stop offset="0" stop-color="#d8dadd"/>
        <stop offset="0.5" stop-color="#8a8f96"/>
        <stop offset="1" stop-color="#c4c7cb"/>
      </linearGradient>
      <linearGradient id="millTone" x1="0" y1="0" x2="1" y2="1">
        <stop offset="0" stop-color="#f0a25a"/>
        <stop offset="0.45" stop-color="#6f7fa8"/>
        <stop offset="1" stop-color="#22375f"/>
      </linearGradient>
    </defs>

    <polygon class="panel-top" points="344,0 860,0 860,523" fill="url(#panelBlue)"/>
    <polygon class="panel-haze" points="560,0 860,0 860,300" fill="#0677BA" opacity="0.35"/>
    <polygon class="accent-left" points="0,323 0,516 206,516" fill="var(--teal)"/>

    <rect class="photo-turbine" role="img" aria-label="Close-up photograph of a jet engine turbine fan"
          x="2" y="-39" width="422" height="422" rx="22" fill="url(#turbineTone)"
          transform="rotate(45 213 172)"/>
    <rect class="tile-blue" x="424" y="231" width="213" height="213" rx="18" fill="#0054AA"
          transform="rotate(45 530 337)"/>
    <rect class="photo-gear" role="img" aria-label="Photograph of a precision machined steel gear"
          x="239" y="390" width="224" height="224" rx="18" fill="url(#gearTone)"
          transform="rotate(45 351 502)"/>

    <polygon class="accent-corner-teal" points="505,1200 860,845 860,885 545,1200" fill="var(--teal)"/>
    <polygon class="accent-corner" points="545,1200 860,885 860,1200" fill="url(#cornerBlue)"/>

    <rect class="photo-milling" role="img" aria-label="Photograph of a CNC milling spindle cutting metal with sparks"
          x="483" y="455" width="438" height="438" rx="22" fill="url(#millTone)"
          transform="rotate(45 702 674)"/>
  </svg>

  <div class="brand">
    <span class="brand__dot"></span>
    <p class="brand__name serif"><span class="line-1">Velbrin</span><span class="line-2">Industries Ltd.</span></p>
  </div>

  <header class="headline serif">
    <h1 class="headline__title">OUR<br>SERVICES</h1>
    <p class="headline__sub">YOUR TEXT HERE</p>
  </header>

  <section class="services">
    <article class="service">
      <svg class="service__icon" viewBox="0 0 46 46" fill="none" stroke="#0b4a8c" stroke-width="2.4" stroke-linecap="round" stroke-linejoin="round">
        <path d="M4 4 V42 H42"/>
        <path d="M11 38 V30 M16 38 V26 M21 38 V29 M26 38 V23 M31 38 V25 M36 38 V20"/>
        <path d="M10 22 L20 13 L26 17 L36 7"/>
        <path d="M30 7 H36 V13"/>
      </svg>
      <div>
        <h2 class="service__title">LOREM IPSUM</h2>
        <p class="service__text">Lorem ipsum dolor sit amet, consectetur adipiscing elit, sed do eiusmod tempor incididunt ut labore et dolore magna aliqua. Ut enim ad minim veniam.</p>
      </div>
    </article>
    <article class="service">
      <svg class="service__icon" viewBox="0 0 46 46" fill="none" stroke="#0b4a8c" stroke-width="2.4" stroke-linecap="round" stroke-linejoin="round">
        <path d="M7 20 A16 16 0 0 1 39 20"/>
        <circle cx="11" cy="27" r="3.5"/><circle cx="23" cy="27" r="3.5"/><circle cx="35" cy="27" r="3.5"/>
        <path d="M5 40 V37 A5 5 0 0 1 17 37 V40 Z"/>
        <path d="M17 40 V37 A5 5 0 0 1 29 37 V40 Z"/>
        <path d="M29 40 V37 A5 5 0 0 1 41 37 V40 Z"/>
      </svg>
      <div>
        <h2 class="service__title">LOREM IPSUM</h2>
        <p class="service__text">Lorem ipsum dolor sit amet, consectetur adipiscing elit, sed do eiusmod tempor incididunt ut labore et dolore magna aliqua. Ut enim ad minim veniam.</p>
      </div>
    </article>
  </section>

  <ul class="contact">
    <li><svg viewBox="0 0 16 16"><path d="M8 1 A5 5 0 0 1 13 6 C13 10 8 15 8 15 C8 15 3 10 3 6 A5 5 0 0 1 8 1 Z M8 4 A2 2 0 1 0 8 8 A2 2 0 1 0 8 4 Z"/></svg>520 Lorem Ipsum Street</li>
    <li><svg viewBox="0 0 16 16"><path d="M3 1 L6 1 L7 5 L5 6.5 C6 9 7 10 9.5 11 L11 9 L15 10 L15 13 C15 14 14 15 13 15 C7 15 1 9 1 3 C1 2 2 1 3 1 Z"/></svg>456 123 789</li>
    <li><svg viewBox="0 0 16 16"><path d="M8 1 A7 7 0 1 1 7.99 1 Z M8 2.4 A5.6 5.6 0 1 0 8.01 2.4 Z M7.3 2.4 H8.7 V13.6 H7.3 Z M2.4 7.3 H13.6 V8.7 H2.4 Z"/></svg>logoname.com</li>
  </ul>

  <blockquote class="quote serif">“Lorem ipsum dolor sit amet,<br>consectetur adipiscing”</blockquote>

  <ul class="social" aria-label="Social media">
    <li></li><li></li><li></li>
  </ul>
</main>
</body>
</html>
```